Business Card Design Project

beauty / make up / lashes

Industry/Entity Type

Business

Contact Information for Business Card

pink / gold / wait / black vintage classic elegant design

```html
<!DOCTYPE html>
<html lang="en">
<head>
<meta charset="UTF-8">
<title>Noa Lashes – Business Card</title>
<link href="https://fonts.googleapis.com/css2?family=Lato:wght@400;700&display=swap" rel="stylesheet">
<style>
  :root {
    --amber: #ffb400;
    --white: #ffffff;
    --paper: #f4f4f4;
    --ink: #111111;
    --stage: #ece9e4;
  }
  * { margin: 0; padding: 0; box-sizing: border-box; }
  html, body { width: 1200px; height: 900px; overflow: hidden; }
  body {
    background: var(--stage);
    font-family: "Lato", sans-serif;
    position: relative;
  }
  .card {
    position: absolute;
    width: 560px;
    height: 320px;
    overflow: hidden;
    box-shadow: 0 6px 18px rgba(0,0,0,0.18);
  }

  /* Front */
  .card--front { left: 50px; top: 120px; background: var(--amber); }
  .brand {
    position: absolute;
    display: flex;
    align-items: center;
    gap: 18px;
    font-weight: 700;
    letter-spacing: 1px;
  }
  .brand__square { width: 46px; height: 46px; }
  .card--front .brand { left: 0; right: 0; top: 66px; justify-content: center; color: var(--white); font-size: 42px; }
  .card--front .brand__square { background: var(--white); }
  .front-band {
    position: absolute;
    left: 0; right: 0;
    top: 186px; height: 78px;
    background: var(--white);
    display: flex; align-items: center; justify-content: center;
  }
  .tagline {
    color: var(--amber);
    font-size: 15px;
    font-weight: 700;
    letter-spacing: 1px;
  }

  /* Back */
  .card--back { left: 590px; top: 460px; background: var(--amber); }
  .back-head {
    position: absolute; left: 0; right: 0; top: 0; height: 136px;
    background: linear-gradient(180deg, var(--white), var(--paper));
  }
  .card--back .brand { left: 0; right: 0; top: 44px; justify-content: center; color: var(--ink); font-size: 40px; }
  .card--back .brand__square { background: var(--amber); }
  .back-rule { position: absolute; left: 0; right: 0; top: 136px; height: 4px; background: var(--ink); }
  .back-gap { position: absolute; left: 0; right: 0; top: 140px; height: 6px; background: var(--white); }

  .person {
    position: absolute; left: 30px; width: 240px; top: 176px;
    text-align: right; color: var(--white);
  }
  .person__name { font-size: 22px; font-weight: 700; }
  .person__role { font-size: 14px; margin-top: 2px; }
  .person__address { font-size: 15px; margin-top: 18px; line-height: 1.4; }

  .contacts {
    position: absolute; left: 308px; top: 180px;
    list-style: none; color: var(--white); font-size: 14px;
  }
  .contacts li { display: flex; align-items: center; gap: 8px; height: 23px; }
  .contacts svg { width: 15px; height: 15px; flex: none; }
</style>
</head>
<body>

  <section class="card card--front">
    <div class="brand"><span class="brand__square"></span>Noa Lashes</div>
    <div class="front-band"><p class="tagline">BEAUTY / MAKE UP / LASHES</p></div>
  </section>

  <section class="card card--back">
    <div class="back-head"></div>
    <div class="brand"><span class="brand__square"></span>Noa Lashes</div>
    <div class="back-rule"></div>
    <div class="back-gap"></div>

    <div class="person">
      <p class="person__name">John Smith</p>
      <p class="person__role">Managing Director</p>
      <p class="person__address">1234, Address GoesHere<br>Country, 12345</p>
    </div>

    <ul class="contacts">
      <li>
        <svg viewBox="0 0 16 16"><rect width="16" height="16" rx="2" fill="#fff"/><path d="M4 5c0-1 1-1.5 2-1.5h4c1 0 2 .5 2 1.5v1H10V5H6v1H4z M5 7h6l1 5H4z" fill="#ffb400"/></svg>
        123-456-7890
      </li>
      <li>
        <svg viewBox="0 0 16 16"><rect width="16" height="16" rx="2" fill="#fff"/><rect x="4" y="3" width="8" height="4" fill="#ffb400"/><rect x="3" y="7" width="10" height="6" rx="1" fill="#ffb400"/></svg>
        123-456-7890
      </li>
      <li>
        <svg viewBox="0 0 16 16"><rect width="16" height="16" rx="2" fill="#fff"/><rect x="3" y="4.5" width="10" height="7" fill="#ffb400"/><path d="M3 4.5l5 4 5-4" stroke="#fff" stroke-width="1" fill="none"/></svg>
        info@youremail.com
      </li>
      <li>
        <svg viewBox="0 0 16 16"><rect width="16" height="16" rx="2" fill="#fff"/><path d="M6 10l4-4M7 5l1-1a2 2 0 0 1 3 3l-1 1M9 11l-1 1a2 2 0 0 1-3-3l1-1" stroke="#ffb400" stroke-width="1.4" fill="none" stroke-linecap="round"/></svg>
        www.yourweb.com
      </li>
    </ul>
  </section>

</body>
</html>
```